Gestatlung flyer (2 pages) format selectable, based accompanying templates (logo, text) Projektflyer "intercultural cooking class with asylum seekers' data Friday evenings 17. 03 / 24.03 / 31.03 / 07.04 / Time: 18:30 Location: KB Merlital St. Gallen Title: Intercultural cooking class with asylum seekers text: cooking course is run by asylum seekers. Cooking together, outlandish specialties, exciting conversations Registration: until 24h before the event costs: Expenses participation at its discretion Logos: Quarzo Linde, Stifung Velmora. The logos should be listed as the sender and do not dominate the flyer. --------- Just be creative, everything is permitted and desired. The goal is that we make as many people as possible aware of this flyer. The flyers are distributed and the target audience is young adults. Dr Flyer should be correspondingly Modern, Emotianal and sales driven (screaming). Strong Typo, clearly legible and the content clearly structured. The shape of the flyer is free! In total we leave you as much creative freedom as possible. I am looking forward to the many great suggestions and am very excited about the results.

Target Market(s)

Young adults

Font styles to use
Serif
Sans Serif
Script

Requirements
Must have
• Textunterstüzung by appropriate images. Friendly design, bright colors. Very easy to read, weighted Title entsrprechend.
Nice to have
• Emotional Cook image or illustration
Should not have
• No picture with white and dark-skinned people.

```html
<!DOCTYPE html>
<html lang="de">
<head>
<meta charset="utf-8">
<title>Interkultureller Kochkurs</title>
<link rel="stylesheet" href="https://fonts.googleapis.com/css2?family=Amatic+SC:wght@700&family=Caveat:wght@600&family=Patrick+Hand+SC&family=Montserrat:wght@400;600&display=swap">
<style>
  :root {
    --page: #ffffff;
    --paper: #d9d9d9;
    --ink: #3a3632;
    --ochre: #d3b92c;
    --ochre-light: #e8d660;
    --icon: #a08c4a;
    --photo-a: #9fa9ad;
    --photo-b: #c9b98a;
    --accent-magenta: #b23a8c;
  }
  html, body { margin: 0; width: 900px; height: 1200px; overflow: hidden; background: var(--page); }
  .flyer {
    position: absolute; left: 62px; top: 35px; width: 788px; height: 1115px;
    background: var(--paper); overflow: hidden;
  }
  .visual {
    position: absolute; left: 178px; top: 40px; width: 432px; height: 753px;
    overflow: hidden;
  }
  .visual svg { position: absolute; inset: 0; }
  .title-band {
    position: absolute; left: 120px; top: 305px; width: 560px; height: 80px;
    background: var(--ochre-light);
    transform: rotate(-27deg); transform-origin: center;
    text-align: center; color: var(--ink);
  }
  .title-band h1 {
    margin: 6px 0 0; font: 700 46px/1 "Amatic SC", sans-serif; letter-spacing: 2px;
  }
  .title-band .subtitle {
    display: block; font: 600 24px/1 "Caveat", cursive; margin-top: -4px;
  }
  .details {
    position: absolute; left: 0; right: 0; top: 830px; text-align: center;
    color: var(--ink); font-family: "Patrick Hand SC", sans-serif;
  }
  .details p { margin: 0; font-size: 23px; line-height: 30px; letter-spacing: 1px; }
  .details .lead { margin-top: 25px; }
  .highlights { list-style: none; padding: 0; margin: 0; font-size: 21px; letter-spacing: 1px; }
  .highlights li { display: inline; margin: 0 8px; }
  .highlights li::before { content: "•"; margin-right: 10px; }
  .practical {
    position: absolute; left: 0; right: 0; top: 997px; text-align: center;
    font: 400 13.5px "Montserrat", sans-serif; color: var(--ink);
  }
  .practical strong { font-weight: 600; }
  .practical .sep { margin: 0 10px; }
  .senders {
    position: absolute; left: 0; right: 0; bottom: 0; height: 73px; background: var(--page);
    display: flex; align-items: center; justify-content: center; gap: 36px;
    font: 600 22px "Montserrat", sans-serif; color: var(--ink);
  }
  .senders .foundation { display: flex; align-items: center; gap: 10px; }
  .senders .foundation i { width: 14px; height: 14px; background: var(--accent-magenta); display: block; }
</style>
</head>
<body>
<main class="flyer">
  <div class="visual">
    <svg viewBox="0 0 432 753" width="432" height="753">
      <defs>
        <linearGradient id="foodTones" x1="0" y1="0" x2="1" y2="1">
          <stop offset="0" stop-color="var(--photo-a)"/>
          <stop offset="1" stop-color="var(--photo-b)"/>
        </linearGradient>
      </defs>
      <rect width="432" height="753" fill="url(#foodTones)" role="img" aria-label="Gedeckter Tisch mit vielen internationalen Speisen von oben"/>
      <polygon points="0,110 432,98 216,360 0,300" fill="var(--ochre)"/>
      <polygon points="216,360 432,290 432,625 0,412" fill="var(--ochre)"/>
      <g class="icon-pot" fill="var(--icon)">
        <path d="M30 230 h110 v8 h-6 v28 a12 12 0 0 1 -12 12 h-74 a12 12 0 0 1 -12 -12 v-28 h-6 z"/>
        <path d="M62 222 q-10 -15 0 -30 q10 -15 0 -30" stroke="var(--icon)" stroke-width="5" fill="none"/>
        <path d="M85 222 q-10 -15 0 -30 q10 -15 0 -30" stroke="var(--icon)" stroke-width="5" fill="none"/>
        <path d="M108 222 q-10 -15 0 -30 q10 -15 0 -30" stroke="var(--icon)" stroke-width="5" fill="none"/>
      </g>
      <g class="icon-cloche" fill="var(--icon)">
        <path d="M325 450 a45 40 0 0 1 90 0 z"/>
        <rect x="318" y="452" width="104" height="7" rx="3"/>
        <circle cx="370" cy="408" r="5"/>
        <path d="M360 395 q-7 -10 0 -20 q7 -10 0 -20 M372 395 q-7 -10 0 -20 q7 -10 0 -20 M384 395 q-7 -10 0 -20 q7 -10 0 -20" stroke="var(--icon)" stroke-width="3" fill="none"/>
      </g>
    </svg>
  </div>
  <div class="title-band">
    <h1>Interkultureller Kochkurs</h1>
    <span class="subtitle">mit asylsuchenden</span>
  </div>

  <section class="details">
    <p>Freitag Abende 17.03 / 24.03 / 31.03 / 07.04/</p>
    <p>Zeit: 18.30h &nbsp;&nbsp;|&nbsp;&nbsp; Ort: KB Merlital St.Gallen</p>
    <p class="lead">Kochkurs wird von Asylsuchenden geleitet.</p>
    <ul class="highlights">
      <li>Gemeinsames Kochen</li>
      <li>Fremdländische Spezialitäten</li>
      <li>Spannende Gespräche</li>
    </ul>
  </section>

  <p class="practical"><strong>Anmeldung:</strong> bis 24h vor dem Anlass<span class="sep">|</span><strong>Kosten:</strong>&nbsp; Unkostenbeteiligung nach eigenem Ermessen</p>

  <footer class="senders">
    <span class="org">Quarzo Linde</span>
    <span class="foundation"><i></i>Stifung Velmora</span>
  </footer>
</main>
</body>
</html>
```